Vor Mask business card

Create a new business card for Vor Mask. Black colour base front and back (the sides can be blue if that works) You can modify the blue colour to best suit the design. I am after a card that looks technical, modern and strong. one side with the Vor Mask and the other company details. The attached file has the details needed for the card. Turnwell is the parent company name and needed but in a smaller size

Target Market(s)

Businesses (suppliers and customers)

Industry/Entity Type

Business

Contact Information for Business Card

Black colour base front and back

Font styles to use
Other font styles liked:
• attached

Requirements
Must have
• Logo's as attached

```html
<!DOCTYPE html>
<html lang="en">
<head>
<meta charset="utf-8">
<title>Vor Mask Business Card</title>
<link href="https://fonts.googleapis.com/css2?family=Montserrat:wght@400;600;700&display=swap" rel="stylesheet">
<style>
  :root {
    --backdrop: #7d7d7d;
    --card-black: #151515;
    --card-edge: #0c0c0c;
    --gloss: #2c2c2c;
    --gloss-light: #3a3a3a;
    --brand-blue: #1e8fd6;
    --text-grey: #9a9a9a;
    --divider: #5a5a5a;
  }
  * { margin: 0; padding: 0; box-sizing: border-box; }
  html, body { width: 802px; height: 1200px; overflow: hidden; }
  body {
    background: var(--backdrop);
    font-family: "Montserrat", sans-serif;
    position: relative;
  }
  .card {
    position: absolute;
    left: 51px;
    width: 700px;
    height: 400px;
    background: var(--card-black);
    border: 1px solid var(--card-edge);
    box-shadow: 0 10px 24px rgba(0,0,0,0.35);
  }
  .card--front { top: 150px; }
  .card--back { top: 650px; }

  .front-brand {
    position: absolute;
    left: 0; right: 0; top: 152px;
    text-align: center;
  }
  .front-brand__name {
    font-family: "Montserrat", sans-serif;
    font-weight: 700;
    font-size: 58px;
    letter-spacing: 5px;
    color: var(--gloss-light);
    line-height: 1;
  }
  .front-brand__tagline {
    margin-top: 14px;
    font-family: "Montserrat", sans-serif;
    font-weight: 700;
    font-size: 16px;
    letter-spacing: 8px;
    color: var(--gloss);
  }

  .parent-brand {
    position: absolute;
    left: 70px; top: 140px;
  }
  .parent-brand__name {
    font-family: "Montserrat", sans-serif;
    font-weight: 700;
    font-size: 46px;
    color: var(--brand-blue);
    line-height: 1;
  }
  .parent-brand__line {
    margin-top: 10px;
    font-size: 11px;
    color: var(--brand-blue);
    letter-spacing: 1px;
  }
  .divider {
    position: absolute;
    left: 360px; top: 70px;
    width: 1px; height: 260px;
    background: var(--divider);
  }
  .contact {
    position: absolute;
    left: 395px; top: 92px;
  }
  .contact__name {
    font-size: 22px;
    font-weight: 600;
    color: var(--brand-blue);
  }
  .contact__role {
    font-size: 13px;
    color: var(--text-grey);
    margin-top: 3px;
    margin-bottom: 18px;
  }
  .contact__row {
    display: flex;
    align-items: flex-start;
    gap: 10px;
    font-size: 13px;
    color: var(--text-grey);
    line-height: 1.35;
    margin-bottom: 9px;
  }
  .contact__icon { flex: 0 0 16px; margin-top: 1px; }
</style>
</head>
<body>
  <section class="card card--front">
    <div class="front-brand">
      <div class="front-brand__name">VOR MASK</div>
      <div class="front-brand__tagline">BUILT FOR THE WORK</div>
    </div>
  </section>

  <section class="card card--back">
    <div class="parent-brand">
      <div class="parent-brand__name">Turnwell</div>
      <div class="parent-brand__line">Technical supply solutions</div>
    </div>
    <div class="divider"></div>
    <div class="contact">
      <div class="contact__name">Owen Hartley</div>
      <div class="contact__role">Managing Director</div>
      <div class="contact__row">
        <svg class="contact__icon" width="16" height="16" viewBox="0 0 16 16"><circle cx="8" cy="8" r="8" fill="#1e8fd6"/><path d="M5.5 4.5l1.5 0 .7 2-1 .8a5 5 0 0 0 2 2l.8-1 2 .7v1.5c0 .4-.4.8-1 .8A6.5 6.5 0 0 1 4.7 5.5c0-.6.4-1 .8-1z" fill="#151515"/></svg>
        <span>+61 400 555 018</span>
      </div>
      <div class="contact__row">
        <svg class="contact__icon" width="16" height="16" viewBox="0 0 16 16"><circle cx="8" cy="8" r="8" fill="#1e8fd6"/><rect x="4" y="5" width="8" height="6" fill="none" stroke="#151515" stroke-width="1.2"/><path d="M4 5l4 3.3L12 5" fill="none" stroke="#151515" stroke-width="1.2"/></svg>
        <span>owen@turnwell.co</span>
      </div>
      <div class="contact__row">
        <svg class="contact__icon" width="16" height="16" viewBox="0 0 16 16"><circle cx="8" cy="8" r="8" fill="#1e8fd6"/><path d="M8 3.5a3 3 0 0 0-3 3c0 2.2 3 5.5 3 5.5s3-3.3 3-5.5a3 3 0 0 0-3-3z" fill="#151515"/><circle cx="8" cy="6.5" r="1" fill="#1e8fd6"/></svg>
        <span>PO Box 208 Keldon<br>NSW 2999<br>Australia</span>
      </div>
      <div class="contact__row">
        <svg class="contact__icon" width="16" height="16" viewBox="0 0 16 16"><circle cx="8" cy="8" r="8" fill="#1e8fd6"/><circle cx="8" cy="8" r="4" fill="none" stroke="#151515" stroke-width="1.1"/><path d="M4 8h8M8 4c-1.6 2.4-1.6 5.6 0 8M8 4c1.6 2.4 1.6 5.6 0 8" fill="none" stroke="#151515" stroke-width="1"/></svg>
        <span>www.turnwell.co</span>
      </div>
    </div>
  </section>
</body>
</html>
```